Webdesign für ORVI Registrierung für die USA
Zielgruppe
Erstellung von Reisegenehmigungen (Visa)
Aufgabenstellung
- Orientierung an Orvi.us
- es gibt kein Logo oder CD
- die Webseite soll seriös wirken

```html
<!DOCTYPE html>
<html lang="de">
<head>
<meta charset="utf-8">
<title>ORVI – Reisegenehmigung USA</title>
<link rel="stylesheet" href="https://fonts.googleapis.com/css2?family=Roboto:wght@300;400;500;700&display=swap">
<style>
:root{
  --navy:#13175a;
  --red:#c8102e;
  --page:#ececec;
  --info-bg:#d8ebf8;
  --text:#333;
  --muted:#555;
  --white:#fff;
}
*{margin:0;padding:0;box-sizing:border-box}
html,body{width:1200px;height:2375px;overflow:hidden}
body{position:relative;background:var(--page);font-family:'Roboto',Arial,sans-serif;color:var(--text)}
.topnav{position:absolute;left:0;top:0;width:1200px;height:37px;background:var(--white);box-shadow:0 2px 3px rgba(0,0,0,.35);z-index:3}
.topnav ul{position:absolute;left:232px;top:10px;display:flex;list-style:none}
.topnav li{font-size:9.5px;font-weight:700;color:var(--navy);padding:0 12px;border-left:1px solid var(--navy);line-height:18px}
.topnav li:first-child{padding-left:0;border-left:none}
.lang{position:absolute;left:880px;top:6px;width:88px;height:24px;border-radius:12px;background:#eee;font-size:9.5px;font-weight:700;color:var(--navy);display:flex;align-items:center;justify-content:center;gap:4px}
.hero{position:absolute;left:0;top:37px;width:1200px;height:726px;background:linear-gradient(180deg,#c9b07a 0%,#e0b45a 18%,#b48a4e 32%,#6e6a62 50%,#4e555c 70%,#3a4148 100%)}
.hero-figure{position:absolute;left:0;top:0;width:420px;height:726px;background:linear-gradient(160deg,#5f7e5a 0%,#476b48 45%,#2f4d36 100%);opacity:.85}
.brand-bar{position:absolute;left:232px;top:131px;width:736px;height:101px;background:var(--white);display:flex;align-items:center}
.brand-mark{width:168px;height:101px;background:var(--navy);color:var(--white);font-size:64px;font-weight:400;display:flex;align-items:center;justify-content:center;letter-spacing:1px}
.brand-text{margin-left:10px}
.brand-text h1{font-size:30px;font-weight:700;color:var(--navy);line-height:32px}
.brand-text p{font-size:18px;font-weight:300;color:var(--navy)}
.btn{display:flex;align-items:center;justify-content:center;gap:6px;background:var(--red);color:var(--white);font-weight:700;border-radius:20px}
.brand-bar .btn{position:absolute;left:566px;top:32px;width:150px;height:37px;font-size:12.5px}
.steps{position:absolute;left:232px;top:509px;width:736px;height:268px;background:var(--white)}
.steps h2{text-align:center;font-size:39px;font-weight:300;color:var(--navy);margin-top:20px}
.track{position:absolute;left:0;top:0;width:736px;height:268px}
.step-label{position:absolute;top:212px;width:190px;text-align:center;font-size:13px;font-weight:500;color:var(--navy);line-height:19px}
.apply{position:absolute;left:232px;top:797px;width:736px;height:282px;background:var(--navy);color:var(--white)}
.apply h2{position:absolute;left:0;top:82px;width:736px;text-align:center;font-size:39px;font-weight:300}
.select{position:absolute;left:189px;top:151px;width:358px;height:37px;background:var(--white);color:var(--navy);font-size:12.5px;font-weight:500;display:flex;align-items:center;justify-content:space-between;padding:0 10px 0 8px}
.apply .btn{position:absolute;left:253px;top:208px;width:231px;height:37px;font-size:12.5px;gap:28px}
.info{position:absolute;left:232px;top:1099px;width:736px;height:496px;background:var(--info-bg);padding:14px 12px;font-size:9.7px;line-height:15px;color:#555}
.info p{margin-bottom:15px}
.cert{position:absolute;left:137px;top:325px;width:461px;height:152px;background:var(--white);font-size:6px;color:#666;overflow:hidden}
.cert-tools{position:absolute;right:8px;top:12px;font-size:6px;color:#888}
.cert-title{position:absolute;left:12px;top:40px;font-weight:700;color:#333}
.cert-note{position:absolute;left:12px;top:52px;width:430px;line-height:8px}
.cert-table{position:absolute;left:12px;top:82px;width:438px;height:38px;border:1px solid #444;display:grid;grid-template-columns:1fr 1fr}
.cert-table div{padding:4px 10px}
.cert-table .head{border-bottom:1px solid #444;font-weight:700;color:#333;height:15px}
.stamp{position:absolute;color:rgba(200,16,46,.35);font-size:22px;font-weight:700;transform:rotate(38deg);letter-spacing:2px}
.faq-head{position:absolute;left:232px;top:1614px;width:736px;height:55px;background:var(--navy);color:var(--white);font-size:31px;font-weight:300;text-align:center;line-height:55px}
.faq-item{position:absolute;left:232px;width:736px;background:var(--white);padding:13px 60px 0 12px}
.faq-item h3{font-size:18.5px;font-weight:500;color:var(--navy);line-height:22px}
.faq-item p{font-size:12.5px;color:var(--muted);line-height:19px;margin-top:6px;width:680px}
.faq-item svg{position:absolute;right:13px}
.footer{position:absolute;left:232px;top:2274px;width:736px;height:101px;background:var(--navy);color:var(--white);font-size:9.5px;text-align:center}
.footer .links{font-weight:700;padding-top:15px;height:32px;border-bottom:1px solid rgba(255,255,255,.8)}
.footer .addr{margin-top:11px}
.footer .copy{margin-top:6px}
</style>
</head>
<body>
<nav class="topnav">
  <ul>
    <li>SO FUNKTIONIERT’S</li><li>ANTRAGSFORMULAR</li><li>INFO</li><li>HÄUFIGE FRAGEN</li><li>KONTAKT</li>
  </ul>
  <div class="lang">DEUTSCH <svg width="9" height="6" viewBox="0 0 9 6"><path d="M1 1l3.5 3.5L8 1" fill="none" stroke="#13175a" stroke-width="1.5"/></svg></div>
</nav>

<div class="hero" role="img" aria-label="Foto: Freiheitsstatue vor der Skyline von New York bei Sonnenuntergang">
  <div class="hero-figure"></div>
</div>

<header class="brand-bar">
  <div class="brand-mark">ORVI</div>
  <div class="brand-text"><h1>United States</h1><p>Travel Authorization Application</p></div>
  <div class="btn">ANTRAG STELLEN <svg width="10" height="10" viewBox="0 0 10 10"><path d="M1 1l4 4-4 4M5 1l4 4-4 4" fill="none" stroke="#fff" stroke-width="1.5"/></svg></div>
</header>

<section class="steps">
  <h2>So funktioniert’s</h2>
  <svg class="track" viewBox="0 0 736 268">
    <line x1="86" y1="175" x2="652" y2="175" stroke="#c8102e" stroke-width="1.5"/>
    <!-- icon 1 -->
    <g transform="translate(63,90)"><rect x="0" y="5" width="46" height="56" rx="3" fill="#13175a"/><rect x="12" y="0" width="22" height="9" rx="2" fill="#13175a" stroke="#fff" stroke-width="2"/><path d="M24 52l24-24 6 6-24 24-8 2z" fill="#fff"/><path d="M27 51l20-20 3 3-20 20-4 1z" fill="#13175a"/><path d="M47 31l3-3 3 3-3 3z" fill="#c8102e"/></g>
    <!-- icon 2 -->
    <g transform="translate(251,90)"><rect x="0" y="5" width="46" height="56" rx="3" fill="#13175a"/><rect x="12" y="0" width="22" height="9" rx="2" fill="#13175a" stroke="#fff" stroke-width="2"/><circle cx="40" cy="47" r="14" fill="#c8102e" stroke="#fff" stroke-width="2"/><path d="M33 47l5 5 9-9" fill="none" stroke="#fff" stroke-width="2.5"/></g>
    <!-- icon 3 -->
    <g transform="translate(430,100)"><rect x="12" y="0" width="52" height="36" rx="5" fill="#13175a"/><line x1="20" y1="9" x2="52" y2="9" stroke="#fff" stroke-width="2" stroke-dasharray="5 3"/><line x1="20" y1="18" x2="34" y2="18" stroke="#fff" stroke-width="2"/><circle cx="46" cy="22" r="5" fill="none" stroke="#fff" stroke-width="2"/><circle cx="52" cy="22" r="5" fill="none" stroke="#fff" stroke-width="2"/><circle cx="14" cy="33" r="14" fill="#c8102e" stroke="#fff" stroke-width="2"/><path d="M7 33l5 5 9-9" fill="none" stroke="#fff" stroke-width="2.5"/></g>
    <!-- icon 4 -->
    <g transform="translate(631,90)"><rect x="0" y="5" width="46" height="56" rx="3" fill="#13175a"/><rect x="12" y="0" width="22" height="9" rx="2" fill="#13175a" stroke="#fff" stroke-width="2"/><circle cx="40" cy="47" r="14" fill="#c8102e" stroke="#fff" stroke-width="2"/><path d="M40 55V40M34 45l6-6 6 6" fill="none" stroke="#fff" stroke-width="2.5"/></g>
    <circle cx="86" cy="175" r="12" fill="#c8102e"/><text x="86" y="180" text-anchor="middle" font-size="12" font-weight="700" fill="#fff" font-family="Roboto,sans-serif">1</text>
    <circle cx="274" cy="175" r="12" fill="#13175a"/><text x="274" y="180" text-anchor="middle" font-size="12" font-weight="700" fill="#fff" font-family="Roboto,sans-serif">2</text>
    <circle cx="464" cy="175" r="12" fill="#13175a"/><text x="464" y="180" text-anchor="middle" font-size="12" font-weight="700" fill="#fff" font-family="Roboto,sans-serif">3</text>
    <circle cx="652" cy="175" r="12" fill="#13175a"/><path d="M647 175l3.5 3.5 6-6" fill="none" stroke="#fff" stroke-width="2"/>
  </svg>
  <div class="step-label" style="left:-9px">Neuen ORVI<br>Antrag stellen</div>
  <div class="step-label" style="left:179px">ORVI Antrag<br>abschließen</div>
  <div class="step-label" style="left:369px">Zahlungsangaben überprüfen<br>und bestätigen</div>
  <div class="step-label" style="left:557px">Antrag eingereicht<br>zur Bearbeitung</div>
</section>

<section class="apply">
  <svg style="position:absolute;left:0;top:0" width="736" height="80" viewBox="0 0 736 80">
    <line x1="87" y1="37" x2="653" y2="37" stroke="#c8102e" stroke-width="1.5"/>
    <circle cx="87" cy="37" r="12" fill="#c8102e"/><text x="87" y="42" text-anchor="middle" font-size="12" font-weight="700" fill="#fff" font-family="Roboto,sans-serif">1</text>
    <circle cx="274" cy="37" r="12" fill="#13175a" stroke="#fff" stroke-width="1.5"/><text x="274" y="42" text-anchor="middle" font-size="12" font-weight="700" fill="#fff" font-family="Roboto,sans-serif">2</text>
    <circle cx="464" cy="37" r="12" fill="#13175a" stroke="#fff" stroke-width="1.5"/><text x="464" y="42" text-anchor="middle" font-size="12" font-weight="700" fill="#fff" font-family="Roboto,sans-serif">3</text>
    <circle cx="653" cy="37" r="12" fill="#13175a" stroke="#fff" stroke-width="1.5"/><path d="M648 37l3.5 3.5 6-6" fill="none" stroke="#fff" stroke-width="2"/>
  </svg>
  <h2>ORVI Antrag:</h2>
  <div class="select">Staatsangehörigkeit des Antragstellers <svg width="16" height="10" viewBox="0 0 16 10"><path d="M2 2l6 6 6-6" fill="none" stroke="#13175a" stroke-width="2.5"/></svg></div>
  <div class="btn">ORVI ANTRAG STELLEN <svg width="10" height="10" viewBox="0 0 10 10"><path d="M1 1l4 4-4 4M5 1l4 4-4 4" fill="none" stroke="#fff" stroke-width="1.5"/></svg></div>
</section>

<section class="info">
  <p>Wir sind darauf spezialisiert, Reisende bei der Beantragung von e-Visen zu unterstützen, um Probleme zu vermeiden und mögliche Fragen zu klären. Wir berechnen pro Antrag eine Bearbeitungsgebühr von USD $ 83,00, wobei dieser Betrag die obligatorische, von der US-Regierung erhobene Gebühr von USD $ 14,00 einschließt. Auf Ihrem Kontoauszug wird ein einziger Betrag ausgewiesen, wie er von unserem Unternehmen erhoben wird. Es steht Ihnen frei, sich von unseren Experten bei der Antragstellung helfen zu lassen. Sie können Ihren Antrag auch selbstständig bei der US-amerikanischen Regierung einreichen: https://orvi.reisegov.us</p>
  <p>Der ORVI Antrag muss elektronisch und online übermittelt werden. Das geschieht, indem Sie ein einfaches, vierstufiges Verfahren durchlaufen. Im ersten und zweiten Schritt wird nach persönlichen Daten gefragt und alle erforderlichen Felder müssen ausgefüllt werden, um mit der Antragstellung fortfahren zu können. Während des dritten Schrittes erfolgt die Zahlung der ORVI Kosten, die sowohl die Bearbeitungsgebühr als auch die Genehmigung an sich abdeckt. Sobald die Zahlung erfolgt ist, erreichen Sie Schritt vier, in dem Sie die Bestätigung über die Übermittlung Ihres ORVI Antrages erhalten. Bitte beachten Sie, dass ORVI kein Visum ist und ein Besuch bei der US-amerikanischen Botschaft nicht erforderlich wird - wie das bisher der Fall war, um ein Visum für die USA zu erhalten. Ihre US ORVI Nummer wird Ihnen per Email zugesandt, was nicht länger als 72 Stunden dauert.</p>
  <p>Diese Reisegenehmigung ist für Sie geeignet, wenn Sie mit geschäftlichen oder touristischen Motiven reisen, durchreisen, aus Gründen im Bereich des Gesundheitswesens oder für kurze Studienaufenthalte (ohne Kredit). Ist die ORVI Genehmigung erteilt, bleibt sie zwei Jahre gültig. Eine Erneuerung ist nach Ablauf dieses Zeitraumes notwendig. Beachten Sie, dass Sie sich trotz der zweijährigen Gültigkeit der ORVI Genehmigung nicht für mehr als 90 Tage nach Einreise und Einreisekontrolle in den Vereinigten Staaten aufhalten dürfen.</p>
  <p>Sobald der Antrag übermittelt und die Zahlung erfolgt ist, erhalten Sie Ihre ORVI Nummer per Email. Diese Nummer ist Ihre Reisegenehmigung. Unten finden Sie</p>
  <div class="cert">
    <div class="cert-tools">Download &nbsp; Print &nbsp; Close ✕</div>
    <div class="cert-title">AUTHORIZATION APPROVED</div>
    <div class="cert-note">Your travel authorization has been approved. A border officer at the port of entry will make the final determination on admission.</div>
    <div class="cert-table">
      <div class="head">APPLICATION NUMBER</div><div class="head">EXPIRATION DATE</div>
      <div>XXXXXXXX00000000</div><div>May 8, 2019</div>
    </div>
    <div class="stamp" style="left:30px;top:50px">SAMPLE</div>
    <div class="stamp" style="left:180px;top:50px">SAMPLE</div>
    <div class="stamp" style="left:330px;top:50px">SAMPLE</div>
  </div>
</section>

<div class="faq-head">Die häufigsten Fragen</div>

<div class="faq-item" style="top:1675px;height:51px"><h3>Was ist eine Reisegenehmigung für die USA?</h3><svg style="top:14px" width="24" height="24" viewBox="0 0 24 24"><circle cx="12" cy="12" r="11" fill="none" stroke="#13175a" stroke-width="2"/><path d="M12 6v12M6 12h12" stroke="#13175a" stroke-width="2.2"/></svg></div>
<div class="faq-item" style="top:1732px;height:107px"><h3>Was ist ein Visa Waiver Land / das Visa Waiver Programm?</h3><p>Das Visa Waiver Programm ist ein Programm der Vereinigten Staaten, dass es Bürgern ausgewählter Länder ermöglicht, ohne Visum in die Vereinigten Staaten zu reisen. Es ist auf Reisen aus geschäftlichen und persönlichen Gründen anwendbar, jedoch nur für Aufenthalte von 90 Tagen oder weniger.</p><svg style="top:12px" width="24" height="24" viewBox="0 0 24 24"><circle cx="12" cy="12" r="11" fill="none" stroke="#13175a" stroke-width="2"/><path d="M6 12h12" stroke="#13175a" stroke-width="2.2"/></svg></div>
<div class="faq-item" style="top:1845px;height:51px"><h3>Welche Länder nehmen am Visa Waiver Programm teil?</h3><svg style="top:14px" width="24" height="24" viewBox="0 0 24 24"><circle cx="12" cy="12" r="11" fill="none" stroke="#13175a" stroke-width="2"/><path d="M12 6v12M6 12h12" stroke="#13175a" stroke-width="2.2"/></svg></div>
<div class="faq-item" style="top:1902px;height:68px"><h3>Wer ist berechtigt, einen ORVI Antrag im Rahmen des Visa Waiver<br>Programms zu stellen?</h3><svg style="top:22px" width="24" height="24" viewBox="0 0 24 24"><circle cx="12" cy="12" r="11" fill="none" stroke="#13175a" stroke-width="2"/><path d="M12 6v12M6 12h12" stroke="#13175a" stroke-width="2.2"/></svg></div>
<div class="faq-item" style="top:1976px;height:51px"><h3>Wie kann ich die ORVI beantragen?</h3><svg style="top:14px" width="24" height="24" viewBox="0 0 24 24"><circle cx="12" cy="12" r="11" fill="none" stroke="#13175a" stroke-width="2"/><path d="M12 6v12M6 12h12" stroke="#13175a" stroke-width="2.2"/></svg></div>
<div class="faq-item" style="top:2033px;height:51px"><h3>Wie wird für ORVI bezahlt?</h3><svg style="top:14px" width="24" height="24" viewBox="0 0 24 24"><circle cx="12" cy="12" r="11" fill="none" stroke="#13175a" stroke-width="2"/><path d="M12 6v12M6 12h12" stroke="#13175a" stroke-width="2.2"/></svg></div>
<div class="faq-item" style="top:2090px;height:51px"><h3>Wie kann die ORVI aktualisiert und verifiziert werden?</h3><svg style="top:14px" width="24" height="24" viewBox="0 0 24 24"><circle cx="12" cy="12" r="11" fill="none" stroke="#13175a" stroke-width="2"/><path d="M12 6v12M6 12h12" stroke="#13175a" stroke-width="2.2"/></svg></div>
<div class="faq-item" style="top:2147px;height:51px"><h3>Was ist zu tun, wenn Ihr ORVI Antrag abgelehnt wurde?</h3><svg style="top:14px" width="24" height="24" viewBox="0 0 24 24"><circle cx="12" cy="12" r="11" fill="none" stroke="#13175a" stroke-width="2"/><path d="M12 6v12M6 12h12" stroke="#13175a" stroke-width="2.2"/></svg></div>
<div class="faq-item" style="top:2204px;height:51px"><h3>Weitere Fragen...</h3><svg style="top:14px" width="24" height="24" viewBox="0 0 24 24"><circle cx="12" cy="12" r="11" fill="none" stroke="#13175a" stroke-width="2"/><path d="M12 6v12M6 12h12" stroke="#13175a" stroke-width="2.2"/></svg></div>

<footer class="footer">
  <div class="links">Datenschutzrichtlinie &nbsp;|&nbsp; Rückstattungsrichtlinie &nbsp;|&nbsp; AGB &nbsp;|&nbsp; Cookies</div>
  <div class="addr">Reisedienst Nord GmbH &nbsp;| &nbsp;Beispielweg 12 &nbsp;| &nbsp;10115 Beispielstadt &nbsp;| &nbsp;Email: info@orviusa.org &nbsp;| &nbsp;Phone: +44 8450001234 &nbsp;| &nbsp;Fax: +44 2030005678</div>
  <div class="copy">© 2017 ORVI APPLICATION SERVICES (www.orvi.us) - All Rights Reserved</div>
</footer>
</body>
</html>
```